Willow Glow & Laser - Business Banner with Brand Elements

Design:
• We would like to get a creative design for a wide banner that will go outside our medical spa clinic location. We need a designer to make a simple yet colorful and high-quality design layout. We want this banner to be eye-catching and to communicate the services we offer at our business: Laser Hair Removal | Velonix | Lip Filler.

Requirements:
• We would like the banner to include our companies information which is the following:

Logo
“Refresh Your Skin”
Laser Hair Removal | Velonix | Lip Filler
(555) 287-1936
www.WillowGlowLaser.com

Colors:
• Our business colors are orange, a hint of black and white, but mostly peach/orange tones. (Orange: #f78f20 , White: #ffffff)

Fonts:
• Josefins Sans Bold & Lato

Content and images can be located here:
https://files.cloudvaultshare.com/folders/7tQmZ2xVbR9kLpN4sW8yH3cD6fJ1gA0eU?usp=sharing

The following will give you an idea of our brand presentation:
• Our website is: www.WillowGlowLaser.com
• Our Instagram; @willowglowlaser
• Our Facebook: www.socialpagehub.com/willowglowlaser

Target Market(s)
• Women 25 - 45

Industry/Entity Type
• Beauty

```html
<!DOCTYPE html>
<html lang="en">
<head>
<meta charset="utf-8">
<title>Willow Glow &amp; Laser – Outdoor Banner</title>
<link rel="stylesheet" href="https://fonts.googleapis.com/css2?family=Josefin+Sans:ital,wght@0,700;1,700&family=Lato:wght@400;700&family=Kaushan+Script&display=swap">
<style>
  :root{
    --orange:#f78f20;
    --orange-soft:#f9a03f;
    --peach:#fbd8ae;
    --cream:#fff7f0;
    --charcoal:#404040;
    --ink:#1a1a1a;
    --white:#ffffff;
    --sky:#56c3e0;
    --blush:#f6cfd6;
  }
  *{margin:0;padding:0;box-sizing:border-box}
  html,body{width:1200px;height:947px;overflow:hidden;background:var(--white)}
  .sheet{position:relative;width:1200px;height:947px}
  .banner{
    position:absolute;left:1px;width:1198px;height:455px;overflow:hidden;
    border:1px solid #9a9a9a;
    background:linear-gradient(90deg,var(--cream) 0%,#fffdfb 45%,var(--white) 70%);
  }
  .banner--dual{top:1px}
  .banner--orange{top:490px}
  .art{position:absolute;inset:0;width:100%;height:100%}
  .brand{position:absolute;left:26px;top:38px;display:flex;align-items:center;gap:14px}
  .brand__mark{width:78px;height:78px;border-radius:50%;background:var(--orange)}
  .brand__name{font-family:"Josefin Sans",sans-serif;font-weight:700;color:var(--ink);line-height:1}
  .brand__name .big{display:block;font-size:62px;letter-spacing:-1px}
  .brand__name .small{display:block;font-size:18px;letter-spacing:7px;margin-top:4px;padding-left:6px}
  .headline{
    position:absolute;left:36px;top:150px;
    font-family:"Kaushan Script",cursive;font-size:86px;line-height:1;letter-spacing:-2px;
    transform:rotate(-4deg);transform-origin:left center;white-space:nowrap;
    text-shadow:3px 3px 0 var(--white),-3px -3px 0 var(--white),3px -3px 0 var(--white),-3px 3px 0 var(--white),5px 7px 8px rgba(0,0,0,.25);
  }
  .headline .lead{color:var(--orange)}
  .headline .tail{color:var(--charcoal)}
  .banner--orange .headline .tail{color:var(--orange)}
  .services{
    position:absolute;left:0;top:325px;width:634px;height:50px;background:var(--orange-soft);
    display:flex;align-items:center;padding-left:24px;
    font-family:"Josefin Sans",sans-serif;font-style:italic;font-weight:700;font-size:31px;color:var(--white);
    white-space:nowrap;letter-spacing:-.5px;
  }
  .services .sep{margin:0 10px;color:var(--ink)}
  .contact{position:absolute;top:384px;left:24px;display:grid;grid-template-columns:360px 260px;row-gap:2px}
  .contact__item{display:flex;align-items:center;gap:12px;height:30px;color:var(--white);white-space:nowrap}
  .contact__item svg{width:24px;height:24px;flex:none}
  .contact__phone{font-family:"Josefin Sans",sans-serif;font-style:italic;font-weight:700;font-size:26px}
  .contact__web{font-family:"Josefin Sans",sans-serif;font-style:italic;font-weight:700;font-size:23px}
  .contact__web .lite{font-weight:400}
  .contact__social{font-family:"Lato",sans-serif;font-size:24px}
  .contact__dot{width:18px;height:18px;border-radius:50%;background:var(--orange);flex:none;margin:0 3px}
</style>
</head>
<body>
<div class="sheet">

  <section class="banner banner--dual">
    <svg class="art" viewBox="0 0 1198 455" aria-hidden="false">
      <defs>
        <radialGradient id="g-beach-a" cx="50%" cy="40%" r="60%"><stop offset="0" stop-color="#e9c3a3"/><stop offset=".5" stop-color="#8fcfdf"/><stop offset="1" stop-color="#4bb6d6"/></radialGradient>
        <radialGradient id="g-city-a" cx="55%" cy="45%" r="60%"><stop offset="0" stop-color="#e7b8a0"/><stop offset=".6" stop-color="#8a6a5a"/><stop offset="1" stop-color="#9a9aa0"/></radialGradient>
        <radialGradient id="g-rose-a" cx="50%" cy="45%" r="60%"><stop offset="0" stop-color="#f1c8b0"/><stop offset="1" stop-color="var(--blush)"/></radialGradient>
      </defs>
      <path d="M783 0H1198V455H900Z" fill="var(--peach)"/>
      <rect x="0" y="375" width="1198" height="80" fill="var(--charcoal)"/>
      <path d="M1080 357H1198V455H1080Z" fill="var(--charcoal)"/>
      <circle cx="1120" cy="425" r="72" fill="var(--orange)"/>
      <circle cx="997" cy="233" r="224" fill="none" stroke="var(--ink)" stroke-width="6" stroke-dasharray="6 5"/>
      <g role="img" aria-label="Photo of a smiling woman in a straw sun hat at the beach">
        <circle cx="997" cy="233" r="206" fill="url(#g-beach-a)"/>
      </g>
      <g role="img" aria-label="Photo of a smiling woman with sunglasses on her head outdoors">
        <circle cx="675" cy="152" r="150" fill="var(--white)"/>
        <circle cx="675" cy="152" r="146" fill="url(#g-city-a)"/>
      </g>
      <g role="img" aria-label="Photo of a woman with glowing skin touching her shoulder on a pink background">
        <circle cx="745" cy="321" r="114" fill="var(--white)"/>
        <circle cx="745" cy="321" r="110" fill="url(#g-rose-a)"/>
      </g>
    </svg>

    <div class="brand">
      <span class="brand__mark"></span>
      <span class="brand__name"><span class="big">Willow</span><span class="small">glow &amp; laser</span></span>
    </div>

    <h1 class="headline"><span class="lead">Refresh</span> <span class="tail">Your Skin</span></h1>

    <p class="services">Laser Hair Removal<span class="sep">/</span>Velonix<span class="sep">/</span>Lip Filler</p>

    <div class="contact">
      <div class="contact__item contact__phone">
        <svg viewBox="0 0 24 24"><path d="M6.6 2.5l3 3.2-1.8 2.4c1.2 2.9 3.3 5 6.2 6.2l2.4-1.8 3.2 3-1.9 3.4C10.6 18.4 5.6 13.4 3.1 4.4z" fill="none" stroke="var(--orange)" stroke-width="1.6" stroke-linejoin="round"/></svg>
        (555) 287-1936
      </div>
      <div class="contact__item contact__social"><span class="contact__dot"></span>@willowglowlaser</div>
      <div class="contact__item contact__web">
        <svg viewBox="0 0 24 24" fill="none" stroke="var(--orange)" stroke-width="1.6"><circle cx="12" cy="12" r="10"/><ellipse cx="12" cy="12" rx="4.5" ry="10"/><path d="M2 12h20M4 6.5h16M4 17.5h16"/></svg>
        <span><span class="lite">www.</span>WillowGlowLaser<span class="lite">.com</span></span>
      </div>
      <div class="contact__item contact__social"><span class="contact__dot"></span>/willowglowlaser</div>
    </div>
  </section>

  <section class="banner banner--orange">
    <svg class="art" viewBox="0 0 1198 455" aria-hidden="false">
      <defs>
        <radialGradient id="g-beach-b" cx="50%" cy="40%" r="60%"><stop offset="0" stop-color="#e9c3a3"/><stop offset=".5" stop-color="#8fcfdf"/><stop offset="1" stop-color="#4bb6d6"/></radialGradient>
        <radialGradient id="g-city-b" cx="55%" cy="45%" r="60%"><stop offset="0" stop-color="#e7b8a0"/><stop offset=".6" stop-color="#8a6a5a"/><stop offset="1" stop-color="#9a9aa0"/></radialGradient>
        <radialGradient id="g-rose-b" cx="50%" cy="45%" r="60%"><stop offset="0" stop-color="#f1c8b0"/><stop offset="1" stop-color="var(--blush)"/></radialGradient>
      </defs>
      <path d="M783 0H1198V455H900Z" fill="var(--peach)"/>
      <rect x="0" y="375" width="1198" height="80" fill="var(--charcoal)"/>
      <path d="M1080 357H1198V455H1080Z" fill="var(--charcoal)"/>
      <circle cx="1120" cy="425" r="72" fill="var(--orange)"/>
      <circle cx="997" cy="233" r="224" fill="none" stroke="var(--ink)" stroke-width="6" stroke-dasharray="6 5"/>
      <g role="img" aria-label="Photo of a smiling woman in a straw sun hat at the beach">
        <circle cx="997" cy="233" r="206" fill="url(#g-beach-b)"/>
      </g>
      <g role="img" aria-label="Photo of a smiling woman with sunglasses on her head outdoors">
        <circle cx="675" cy="152" r="150" fill="var(--white)"/>
        <circle cx="675" cy="152" r="146" fill="url(#g-city-b)"/>
      </g>
      <g role="img" aria-label="Photo of a woman with glowing skin touching her shoulder on a pink background">
        <circle cx="745" cy="321" r="114" fill="var(--white)"/>
        <circle cx="745" cy="321" r="110" fill="url(#g-rose-b)"/>
      </g>
    </svg>

    <div class="brand">
      <span class="brand__mark"></span>
      <span class="brand__name"><span class="big">Willow</span><span class="small">glow &amp; laser</span></span>
    </div>

    <h2 class="headline"><span class="lead">Refresh</span> <span class="tail">Your Skin</span></h2>

    <p class="services">Laser Hair Removal<span class="sep">/</span>Velonix<span class="sep">/</span>Lip Filler</p>

    <div class="contact">
      <div class="contact__item contact__phone">
        <svg viewBox="0 0 24 24"><path d="M6.6 2.5l3 3.2-1.8 2.4c1.2 2.9 3.3 5 6.2 6.2l2.4-1.8 3.2 3-1.9 3.4C10.6 18.4 5.6 13.4 3.1 4.4z" fill="none" stroke="var(--orange)" stroke-width="1.6" stroke-linejoin="round"/></svg>
        (555) 287-1936
      </div>
      <div class="contact__item contact__social"><span class="contact__dot"></span>@willowglowlaser</div>
      <div class="contact__item contact__web">
        <svg viewBox="0 0 24 24" fill="none" stroke="var(--orange)" stroke-width="1.6"><circle cx="12" cy="12" r="10"/><ellipse cx="12" cy="12" rx="4.5" ry="10"/><path d="M2 12h20M4 6.5h16M4 17.5h16"/></svg>
        <span><span class="lite">www.</span>WillowGlowLaser<span class="lite">.com</span></span>
      </div>
      <div class="contact__item contact__social"><span class="contact__dot"></span>/willowglowlaser</div>
    </div>
  </section>

</div>
</body>
</html>
```